Bright Harbor Counseling Letterhead for hip modern business

I would like some ombre use of the colors in the logo hip letterhead that incorporates logo colors and feel, needs to connect with young professionals and college students. i need to be able to write letters to schools to excuse absences as well. i like color blocks on one side preferably using colors from the attached logo design.

Target Market(s)

high income young people, young adults and college students

Industry/Entity Type

mental health

Font styles to use
Serif
Sans Serif

Colors
0054AA
0677BA
7BADD7
CADEEF
E8F1F8
0094D4
00A9DD
6FCCEA
C7EBF8
E9F6FB
00AB8E
00BBA5
67D7C9
C6EFE9
E9F9F6
59FF00
82FF00
B8FF75
E3FFCB
F4FFEA
A7469A
B969AE
D3A5CF
EDDBEB
F8F0F9
6B429C
8869AF
B7A5CE
E3DAEB
F3F0F8

Requirements
Must have
• a modern hip feel, somewhat color

```html
<!DOCTYPE html>
<html lang="en">
<head>
<meta charset="utf-8">
<title>Bright Harbor Counseling Letterhead</title>
<link rel="stylesheet" href="https://fonts.googleapis.com/css2?family=Montserrat:wght@300;400&family=Arimo:wght@400&display=swap">
<style>
  :root {
    --backdrop: #a9c8e4;
    --paper: #ffffff;
    --ink: #222222;
    --ink-soft: #555555;
    --ink-muted: #9a9a9a;
    --teal: #00bba5;
    --teal-light: #67d7c9;
    --blue: #0677ba;
    --sky: #00a9dd;
    --purple: #6b429c;
    --magenta: #a7469a;
    --rule: #555555;
  }
  * { box-sizing: border-box; margin: 0; padding: 0; }
  html, body { width: 1200px; height: 900px; overflow: hidden; }
  body {
    background: var(--backdrop);
    font-family: "Montserrat", sans-serif;
    position: relative;
  }
  .letterhead {
    position: absolute;
    left: 313px; top: 42px;
    width: 574px; height: 811px;
    background: var(--paper);
    overflow: hidden;
  }
  .decor-top {
    position: absolute; left: 0; top: 0;
    width: 160px; height: 100px;
    border-bottom-right-radius: 100% 100%;
    background: linear-gradient(135deg, var(--purple) 0%, var(--magenta) 55%, var(--teal-light) 100%);
    opacity: .75;
  }
  .decor-bottom {
    position: absolute; right: 0; bottom: 0;
    width: 202px; height: 126px;
    border-top-left-radius: 100% 100%;
    background: linear-gradient(135deg, var(--sky) 0%, var(--teal) 30%, var(--blue) 60%, var(--magenta) 100%);
    opacity: .8;
  }
  .brand {
    position: absolute; left: 38px; top: 100px;
    display: flex; align-items: center; gap: 7px;
  }
  .brand-dot {
    width: 12px; height: 12px; border-radius: 50%;
    background: var(--purple);
  }
  .brand-name {
    font-weight: 300; font-size: 17px; color: var(--ink);
    letter-spacing: .2px; white-space: nowrap;
  }
  .contact {
    position: absolute; left: 439px; top: 38px;
    border-left: 1px solid var(--rule);
    padding-left: 9px; height: 54px;
    font-family: "Arimo", sans-serif; font-size: 7.5px; color: var(--ink);
    line-height: 9.5px;
  }
  .contact-address { margin-bottom: 5px; }
  .contact-line { display: flex; align-items: center; gap: 4px; }
  .contact-line svg { width: 6px; height: 6px; fill: var(--teal); flex: none; }
  .recipient { position: absolute; left: 59px; top: 180px; }
  .to-label { font-size: 11px; letter-spacing: 1.5px; color: var(--ink); margin-bottom: 4px; }
  .recipient-name { font-size: 9.5px; color: var(--teal); margin-bottom: 4px; }
  .recipient-line { font-size: 7px; font-weight: 300; color: var(--ink-muted); line-height: 12.5px; }
  .date {
    position: absolute; right: 58px; top: 180px;
    font-size: 8px; color: var(--ink-soft);
  }
  .body-copy {
    position: absolute; left: 59px; top: 290px; width: 458px;
    font-size: 7.5px; font-weight: 300; line-height: 10.2px;
    color: var(--ink-muted); text-align: justify;
  }
  .body-copy p { margin-bottom: 10px; }
  .signature-mark {
    position: absolute; left: 58px; top: 575px;
    width: 100px; height: 22px; border-radius: 11px;
    background: linear-gradient(90deg, #e6e6e6, #f4f4f4);
  }
  .signer { position: absolute; left: 57px; top: 604px; }
  .signer-name { font-size: 9px; color: var(--ink); margin-bottom: 2px; }
  .signer-role { font-size: 7px; font-weight: 300; color: var(--ink-muted); }
</style>
</head>
<body>
  <main class="letterhead">
    <div class="decor-top" role="img" aria-label="Overlapping translucent bubble decoration in purple and teal"></div>

    <div class="brand">
      <span class="brand-dot"></span>
      <span class="brand-name">Bright Harbor Counseling</span>
    </div>

    <address class="contact">
      <div class="contact-address">Your address, city<br>state, ZIP 0000</div>
      <div class="contact-line">
        <svg viewBox="0 0 10 10"><path d="M2 0.5 L3.8 2.6 L2.9 3.8 C3.6 5.3 4.7 6.4 6.2 7.1 L7.4 6.2 L9.5 8 L8.2 9.5 C4.2 9 1 5.8 0.5 1.8 Z"/></svg>
        <span>123-456-2100</span>
      </div>
      <div class="contact-line">
        <svg viewBox="0 0 10 10"><path d="M0.5 2 H9.5 V8 H0.5 Z M0.5 2 L5 5.5 L9.5 2" fill="none" stroke="#00bba5" stroke-width="1.2"/></svg>
        <span>hello@brightharbor.com</span>
      </div>
      <div class="contact-line">
        <svg viewBox="0 0 10 10"><circle cx="5" cy="5" r="4.3" fill="none" stroke="#00bba5" stroke-width="1.2"/><path d="M0.7 5 H9.3 M5 0.7 V9.3" stroke="#00bba5" stroke-width="1"/></svg>
        <span>www.yourwebsite.com</span>
      </div>
    </address>

    <section class="recipient">
      <div class="to-label">TO</div>
      <div class="recipient-name">Dana Whitfield</div>
      <div class="recipient-line">Human Resources</div>
      <div class="recipient-line">Northgate Studio Inc.</div>
      <div class="recipient-line">2250-B Linden Row, Fairhaven</div>
      <div class="recipient-line">E42 USA</div>
    </section>

    <div class="date">Friday, 01/01/2018</div>

    <article class="body-copy">
      <p>Lorem ipsum dolor sit amet, consectetuer adipiscing elit, sed diam nonummy nibh euismod tincidunt ut laoreet dolore magna aliquam erat volutpat. Ut wisi enim ad minim veniam, quis nostrud exerci tation ullamcorper suscipit lobortis nisl ut aliquip ex ea commodo consequat. Duis autem vel eum iriure dolor in hendrerit in vulputate velit esse molestie consequat, vel illum dolore eu feugiat nulla facilisis at vero eros et accumsan et iusto odio dignissim qui blandit praesent luptatum zzril delenit augue duis dolore te feugait nulla facilisi.</p>
      <p>Nam liber tempor cum soluta nobis eleifend option congue nihil imperdiet doming id quod mazim placerat facer possim assum. Typi non habent claritatem insitam;</p>
      <p>Est usus legentis in iis qui facit eorum claritatem.</p>
      <p>Investigationes demonstraverunt lectores legere me lius quod ii legunt saepius. Claritas est etiam processus dynamicus, qui sequitur mutationem consuetudium lectorum. Mirum est notare quam littera gothica, quam nunc putamus parum claram, anteposuerit litterarum formas humanitatis per seacula quarta decima et quinta decima. Eodem modo typi, qui nunc nobis videntur parum clari, fiant sollemnes in futurum.</p>
      <p>consectetuer adipiscing elit, sed diam nonummy nibh euismod tincidunt ut laoreet dolore magna aliquam erat volutpat. Ut wisi enim ad minim veniam, quis nostrud exerci tation ullamcorper suscipit lobortis nisl ut aliquip ex ea commodo consequat. Duis autem vel eum iriure dolor in hendrerit in vulputate velit esse molestie consequat, vel illum dolore eu feugiat nulla facilisis at vero eros et accumsan et iusto odio dignissim qui blandit praesent luptatum zzril delenit augue duis dolore te feugait nulla facilisi.</p>
      <p>Nam liber tempor cum soluta nobis eleifend option congue nihil imperdiet.</p>
    </article>

    <div class="signature-mark" role="img" aria-label="Handwritten signature of Owen Carlisle"></div>
    <div class="signer">
      <div class="signer-name">Owen Carlisle</div>
      <div class="signer-role">Managing Director</div>
    </div>

    <div class="decor-bottom" role="img" aria-label="Overlapping translucent bubble decoration in sky blue, teal, navy and magenta"></div>
  </main>
</body>
</html>
```